まず、縦を想定しており、画像をメインにした構成を想定しております。

上半分は覚悟を決めた中年以上の料理にが仁王立ちしているようなイメージの写真で「店を売るという選択」or「店をゆずる決断」というキャプション

下半分はやる気に満ち溢れた若者が覚悟を持って仁王立ちしているようなイメージ
「店を買う」or「店(歴史)を引きつぐ覚悟」というキャプション

そして、下の方に計算式添付の資料にあるような表を挿入。
売却した方は結局、いくら得したのか。買った方はいくら得したのかがわかるように。あとは、「査定無料」「神奈川エリアに特化した唯一のエージェントです」を記載お願いします。最後にヴェルコハーバーズという社名と連絡先を記載。

全体的なイメージではノルヴェクや外国の広告のようにシンプルだけどもどこかデザイン性を感じるように。また、信頼性も大事なので全体的にシックだけども目を引くように。
VELKO HARBORS
ヴェルコハーバーズ
0120-471-362
www.velko-harbors-jp.example
A4
片面
青系、茶系、グレー系
• 高解像度JPG (.jpg)
• イラストレーター形式 (.ai)
キャプションの修正
【メインキャプション】大事なお店、最も高く売却いたします。
【売手側キャプション】 お店を売るという選択
【買手側キャプション】お店を買うという選択

また、各キャプションを大きめに表示をお願いします。

全体的にまとまっており、柔軟に対応頂いたため。

ありがとうござました!!

```html
<!DOCTYPE html>
<html lang="ja">
<head>
<meta charset="utf-8">
<title>ヴェルコハーバーズ SELL × BUY</title>
<link rel="stylesheet" href="https://fonts.googleapis.com/css2?family=Noto+Sans+JP:wght@400;500;700;900&family=Montserrat:wght@300;500;600;700&display=swap">
<style>
  :root {
    --brown-dark: #2b1f18;
    --brown-mid: #6b4a36;
    --brown-light: #a87a57;
    --blue-dark: #1c2b3a;
    --blue-mid: #3d5d7a;
    --blue-light: #7f9fb9;
    --white: #ffffff;
    --ink: #1d1d1d;
    --table-line: rgba(255,255,255,0.35);
    --table-head: rgba(255,255,255,0.18);
  }
  * { margin: 0; padding: 0; box-sizing: border-box; }
  html, body { width: 849px; height: 1200px; overflow: hidden; background: #222; }
  .poster {
    position: relative; width: 849px; height: 1200px; overflow: hidden;
    font-family: "Noto Sans JP", sans-serif; color: var(--white);
  }
  .half { position: absolute; top: 0; height: 1200px; width: 425px; }
  .half--seller { left: 0; background: linear-gradient(180deg, #5a3f2e 0%, var(--brown-mid) 30%, #4a3326 58%, var(--brown-dark) 100%); }
  .half--buyer { left: 424px; background: linear-gradient(180deg, #4f6e8a 0%, var(--blue-mid) 30%, #2e455b 58%, var(--blue-dark) 100%); }
  .photo { position: absolute; top: 0; height: 740px; }
  .photo--seller {
    left: 0; width: 425px;
    background: radial-gradient(ellipse 60% 55% at 55% 45%, var(--brown-light) 0%, var(--brown-mid) 45%, rgba(43,31,24,0) 85%);
  }
  .photo--buyer {
    left: 424px; width: 425px;
    background: radial-gradient(ellipse 55% 55% at 45% 40%, var(--blue-light) 0%, var(--blue-mid) 45%, rgba(28,43,58,0) 85%);
  }
  .brand {
    position: absolute; left: 20px; top: 20px; display: flex; align-items: center; gap: 8px;
  }
  .brand-mark { width: 18px; height: 18px; background: var(--white); }
  .brand-name { font-family: "Montserrat", sans-serif; font-weight: 700; font-size: 13px; letter-spacing: 1px; }
  .caption {
    position: absolute; top: 30px; writing-mode: vertical-rl;
    font-weight: 700; font-size: 24px; letter-spacing: 4px;
  }
  .caption--seller { left: 108px; }
  .caption--buyer { left: 476px; }
  .headline {
    position: absolute; top: 612px; left: 0; width: 849px; height: 150px;
    font-family: "Montserrat", sans-serif; font-weight: 600; font-size: 150px; line-height: 150px;
  }
  .headline-sell { position: absolute; left: 30px; letter-spacing: 4px; }
  .headline-buy { position: absolute; left: 452px; letter-spacing: 30px; }
  .headline-cross { position: absolute; left: 396px; top: 38px; width: 70px; height: 70px; }
  .savings { position: absolute; top: 790px; width: 350px; }
  .savings--seller { left: 36px; }
  .savings--buyer { left: 462px; }
  .savings-label { font-size: 10px; margin-bottom: 3px; }
  .savings-table { width: 100%; border-collapse: collapse; font-size: 10px; }
  .savings-table th, .savings-table td {
    border-bottom: 1px solid var(--table-line); padding: 4px 5px; font-weight: 400; text-align: center; height: 20px;
  }
  .savings-table thead th { background: var(--table-head); }
  .savings-table tbody th { text-align: left; background: rgba(255,255,255,0.08); }
  .savings-table tr.total th, .savings-table tr.total td { background: rgba(255,255,255,0.22); font-weight: 700; }
  .savings-result { margin-top: 8px; font-weight: 900; font-size: 25px; letter-spacing: 0.5px; }
  .savings-result small { font-size: 17px; font-weight: 700; }
  .footer-left { position: absolute; left: 30px; top: 1110px; display: flex; gap: 12px; align-items: center; }
  .badge-free {
    background: var(--white); color: var(--ink); font-weight: 700; font-size: 13px;
    width: 62px; height: 62px; display: flex; align-items: center; justify-content: center;
  }
  .agent-note { font-size: 9px; margin-bottom: 6px; }
  .agent-name { font-weight: 700; font-size: 14px; line-height: 1.35; }
  .footer-right { position: absolute; right: 28px; top: 1120px; text-align: right; font-family: "Montserrat", sans-serif; }
  .footer-brand { font-weight: 500; font-size: 14px; letter-spacing: 4px; margin-bottom: 6px; }
  .footer-tel { font-weight: 700; font-size: 22px; letter-spacing: 1px; }
  .footer-tel span { font-size: 13px; margin-right: 6px; }
  .footer-web { font-weight: 600; font-size: 12px; letter-spacing: 1px; margin-top: 3px; }
</style>
</head>
<body>
<div class="poster">
  <div class="half half--seller"></div>
  <div class="half half--buyer"></div>
  <div class="photo photo--seller" role="img" aria-label="腕を組んで仁王立ちする年配の料理人の写真"></div>
  <div class="photo photo--buyer" role="img" aria-label="腕を組んで仁王立ちする若い料理人の写真"></div>

  <div class="brand">
    <span class="brand-mark"></span>
    <span class="brand-name">VELKO HARBORS</span>
  </div>

  <h2 class="caption caption--seller">店を「売る」という決断。</h2>
  <h2 class="caption caption--buyer">店を「買う」という覚悟。</h2>

  <h1 class="headline">
    <span class="headline-sell">SELL</span>
    <svg class="headline-cross" viewBox="0 0 70 70"><line x1="5" y1="5" x2="65" y2="65" stroke="#fff" stroke-width="2"/><line x1="65" y1="5" x2="5" y2="65" stroke="#fff" stroke-width="2"/></svg>
    <span class="headline-buy">BUY</span>
  </h1>

  <section class="savings savings--seller">
    <p class="savings-label">閉店コスト</p>
    <table class="savings-table">
      <thead><tr><th>シミュレーション</th><th>通常閉店</th><th>弊社サービス</th></tr></thead>
      <tbody>
        <tr><th>解約後賃料負担</th><td>-450,000円</td><td>0円</td></tr>
        <tr><th>内装解体費用</th><td>-550,000円</td><td>0円</td></tr>
        <tr><th>造作売却代金</th><td>0円</td><td>2,000,000円</td></tr>
        <tr class="total"><th>合計</th><td>-1,000,000円</td><td>2,000,000円</td></tr>
      </tbody>
    </table>
    <p class="savings-result">3,000,000円<small>のメリット</small></p>
  </section>

  <section class="savings savings--buyer">
    <p class="savings-label">開店コスト</p>
    <table class="savings-table">
      <thead><tr><th>シミュレーション</th><th>通常開店</th><th>弊社サービス</th></tr></thead>
      <tbody>
        <tr><th>内装設備費用</th><td>13,000,000円</td><td>0円</td></tr>
        <tr><th>造作購入代金</th><td>0円</td><td>3,500,000円</td></tr>
        <tr><th>保証金差額</th><td>0円</td><td>0円</td></tr>
        <tr class="total"><th>合計</th><td>13,000,000円</td><td>3,500,000円</td></tr>
      </tbody>
    </table>
    <p class="savings-result">9,500,000円<small>のコストダウン</small></p>
  </section>

  <div class="footer-left">
    <div class="badge-free">査定無料</div>
    <div>
      <p class="agent-note">神奈川エリアに特化した唯一のエージェントです</p>
      <p class="agent-name">店舗売買仲介サービスの<br>ヴェルコハーバーズ</p>
    </div>
  </div>

  <div class="footer-right">
    <p class="footer-brand">VELKO HARBORS</p>
    <p class="footer-tel"><span>TEL.</span>0120-471-362</p>
    <p class="footer-web">www.velko-harbors-jp.example</p>
  </div>
</div>
</body>
</html>
```